Umbrian Friars Roast: a new roasting company in Italy by real monks.

We need a logo and label design for a new coffee roastery in Italy, near Florence. We are real monks that roast coffee with wood. Very high quality. We would like to receive proposal for the logo "Umbrian Friars roast" design and labels. In the logo design a monk in black must be present but it must not be something serious or sad. The logo must have the writing "Umbrian Friars roast" more important and less important "Cloister of Stillwater". We like something similar to the attached logo but the monk can also be seen in the face and more smiling. Italianness could be expressed on the labels but not banal (see Tuscan mountains). About the label: Our customers must first buy the beauty of the package and labels and then taste the coffee. It could be something particular like the attachment that we really like or something modern. The important thing is that the labels must be beautiful, even colorful but sober and elegant. Attached you will find the text on the front and back of the label. You can visit our web site www.chiostrodellaquiete.it but the coffee is at the beginning, please visit our facebook https://www.facebook.com/www.prioratodivalleombrosa.org
IMPORTANT: We will not design the whole package but only a label on a neutral black package as attacched. What is important now is not the size of the package but the idea.
Now we just need an idea. The winner will be invited to a 1:1 job to perfect the labels of the 7 blends.

Target Market(s)

Retail

Industry/Entity Type

coffee

Requirements
Must have
• Monk design
Nice to have
• Something of special

```html
<!DOCTYPE html>
<html lang="en">
<head>
<meta charset="utf-8">
<title>Umbrian Friars Roast – The Aurora Blend labels</title>
<link href="https://fonts.googleapis.com/css2?family=Montserrat:wght@400;600;700&family=Roboto+Condensed:wght@400;500&family=Berkshire+Swash&display=swap" rel="stylesheet">
<style>
  :root{
    --backdrop:#e8e5e0;
    --bag:#111111;
    --brown:#5a3417;
    --brown-soft:#7a5232;
    --cream:#f3ece2;
    --panel:rgba(236,236,232,.86);
    --flag-green:#1f8a3e;
    --flag-red:#cc2229;
    --ink:#2d2119;
  }
  *{box-sizing:border-box;margin:0;padding:0}
  html,body{width:1200px;height:900px;overflow:hidden}
  body{background:var(--backdrop);font-family:"Montserrat",sans-serif;color:var(--ink);position:relative}

  .bag{position:absolute;top:30px;width:520px;height:840px;background:var(--bag);border-radius:6px}
  .bag--front{left:50px}
  .bag--back{left:630px}
  .label{position:absolute;left:20px;right:20px;top:230px;bottom:20px;overflow:hidden}

  .scenery{position:absolute;inset:0}
  .front .scenery{
    background:
      radial-gradient(ellipse 42% 6% at 22% 20%, rgba(255,255,255,.6), transparent 70%),
      radial-gradient(ellipse 38% 6% at 80% 27%, rgba(255,255,255,.55), transparent 70%),
      radial-gradient(ellipse 30% 4% at 60% 8%, rgba(255,255,255,.35), transparent 70%),
      linear-gradient(180deg,#2f69a8 0%,#5d93c6 12%,#c9dcea 26%,#9bb9d4 30%,#5479a8 35%,#3f638f 42%,#63876a 47%,#8fb04a 53%,#c2b94e 59%,#86a43c 65%,#3f6a2a 73%,#5a832f 85%,#3b5c21 100%);
  }
  .back .scenery{
    background:
      radial-gradient(ellipse 30% 12% at 8% 20%, rgba(255,255,255,.7), transparent 70%),
      radial-gradient(ellipse 30% 12% at 95% 18%, rgba(255,255,255,.7), transparent 70%),
      linear-gradient(180deg,#4a86c0 0%,#9cc3e0 18%,#dfe9ef 28%,#7f9fb8 34%,#7da45a 42%,#5f8f36 60%,#8bb44a 75%,#4f7a2a 100%);
  }

  .logo{position:absolute;left:0;right:0;text-align:center;color:var(--brown)}
  .logo__mark{display:block;margin:0 auto 8px;border-radius:50%;background:#4a2c14;border:4px solid var(--cream)}
  .logo__name{font-weight:700;text-transform:uppercase;letter-spacing:.06em;color:var(--brown);line-height:1.25}
  .logo__sub{display:block;font-size:11px;letter-spacing:.12em}

  /* front */
  .front .logo{top:28px}
  .front .logo__mark{width:150px;height:150px}
  .front .logo__name{font-size:22px}
  .info{position:absolute;left:36px;right:36px;bottom:46px;background:var(--cream);
    border:5px solid var(--brown);border-radius:22px;padding:10px 12px 8px;color:var(--brown)}
  .info__head{display:flex;align-items:center;gap:10px}
  .badge{width:40px;height:40px;border-radius:50%;background:var(--brown);flex:none}
  .info__title{flex:1;text-align:center}
  .blend{font-family:"Berkshire Swash",cursive;font-size:27px;color:var(--brown)}
  .subtitle{font-size:10px;font-style:italic;color:var(--brown-soft)}
  .flag{display:flex;width:22px;height:30px;flex:none}
  .flag span{flex:1}
  .specs{display:flex;border-top:1px solid var(--brown-soft);border-bottom:1px solid var(--brown-soft);margin-top:6px;font-size:10px}
  .specs div{padding:4px 6px;border-right:1px solid var(--brown-soft)}
  .specs div:last-child{border-right:none}
  .specs b{font-weight:700}
  .desc{font-size:9.5px;line-height:1.35;padding:6px 2px;color:var(--ink)}
  .roast{display:flex;justify-content:space-between;font-size:9.5px;padding:4px 2px 6px;border-bottom:1px solid var(--brown-soft)}
  .roast span{display:flex;align-items:center;gap:4px}
  .box{width:9px;height:9px;border:1px solid var(--brown);display:inline-block;position:relative}
  .box--on::after{content:"";position:absolute;inset:2px;background:var(--brown)}
  .dots{letter-spacing:1px;color:var(--brown)}
  .foot{display:flex;align-items:center;font-size:8px;text-align:center;color:var(--brown-soft)}
  .foot div{padding:5px 4px;flex:1;border-right:1px solid var(--brown-soft)}
  .foot .weight{flex:none;border:none;font-size:22px;color:var(--ink);padding-left:8px}
  .site{position:absolute;left:16px;bottom:8px;font-size:8px;color:#fff}

  /* back */
  .sheet{position:absolute;left:34px;right:34px;top:44px;bottom:50px;background:var(--panel);border-radius:26px}
  .back .logo{top:14px}
  .back .logo__mark{width:90px;height:90px}
  .back .logo__name{font-size:15px}
  .seal{position:absolute;top:60px;width:52px;height:52px;border-radius:50%}
  .seal--left{left:28px;background:var(--brown)}
  .seal--right{right:28px;background:var(--flag-green)}
  .back-copy{position:absolute;left:22px;right:22px;top:150px;color:var(--brown)}
  .back-copy h2{font-size:9.5px;font-weight:700;text-align:center;line-height:1.4;margin-bottom:8px}
  .story{font-family:"Roboto Condensed",sans-serif;font-size:9.4px;line-height:1.32;text-transform:uppercase;text-align:justify;color:var(--ink)}
  .story p+p{margin-top:3px}
  .legal{position:absolute;left:22px;right:22px;bottom:40px;border-top:1px solid var(--brown-soft);border-bottom:1px solid var(--brown-soft);display:flex;font-size:7.5px;color:var(--ink)}
  .legal__origin{flex:1;padding:5px 4px;line-height:1.35;border-right:1px solid var(--brown-soft)}
  .legal__care{width:100px;padding:5px 6px;color:var(--brown-soft)}
  .legal__care svg{margin-top:4px}
  .urls{position:absolute;left:0;right:0;bottom:22px;text-align:center;font-size:8px;color:var(--ink)}
  .net{position:absolute;left:0;right:0;bottom:4px;text-align:center;font-size:10px;color:var(--ink)}
  .best{position:absolute;left:28px;bottom:10px;width:150px;height:30px;background:#fff;font-size:9px;padding:8px;color:var(--ink)}
</style>
</head>
<body>

<section class="bag bag--front">
  <div class="label front">
    <div class="scenery" role="img" aria-label="Illustrated Tuscan landscape: blue sky with clouds, layered blue mountains, green and golden rolling hills with a small village, cypress trees and wildflowers"></div>

    <div class="logo">
      <span class="logo__mark" role="img" aria-label="Smiling monk portrait emblem"></span>
      <div class="logo__name">Umbrian Friars Roast<span class="logo__sub">Cloister of Stillwater</span></div>
    </div>

    <div class="info">
      <div class="info__head">
        <span class="badge" role="img" aria-label="Handmade seal"></span>
        <div class="info__title">
          <div class="blend">The Aurora Blend</div>
          <div class="subtitle">100% Wood Roasted Arabica Coffee</div>
        </div>
        <div class="flag" aria-label="Italian colours"><span style="background:var(--flag-green)"></span><span style="background:#fff"></span><span style="background:var(--flag-red)"></span></div>
      </div>
      <div class="specs">
        <div><b>Process:</b> Wood Roasted</div>
        <div><b>Region:</b> Tuscany</div>
        <div><b>Level:</b> High</div>
      </div>
      <p class="desc">Indulge in our 100% Arabica coffee blend, featuring sweet, exotic fruit and spice notes, medium-strong intensity, and lively citrus and floral hints of orange and bergamot</p>
      <div class="roast">
        <span><i class="box"></i><span class="dots">●●●●●</span> Light</span>
        <span><i class="box box--on"></i><span class="dots">●●●●●</span> Medium</span>
        <span><i class="box"></i><span class="dots">●●●●●</span> Dark</span>
      </div>
      <div class="foot">
        <div>Roasted to order,<br>just before shipping</div>
        <div>Italian High Quality Coffee<br>Roasted by the Friars of the<br>Cloister of Stillwater in Tuscany</div>
        <div class="weight">250gr</div>
      </div>
    </div>
    <div class="site">www.umbrianfriars.coffee</div>
  </div>
</section>

<section class="bag bag--back">
  <div class="label back">
    <div class="scenery" role="img" aria-label="Illustrated green Tuscan hills with vineyards under a bright sky with clouds"></div>
    <div class="sheet">
      <div class="logo">
        <span class="logo__mark" role="img" aria-label="Smiling monk portrait emblem"></span>
        <div class="logo__name">Umbrian Friars Roast</div>
      </div>
      <span class="seal seal--left" role="img" aria-label="Handmade seal"></span>
      <span class="seal seal--right" role="img" aria-label="Nature respect seal"></span>

      <div class="back-copy">
        <h2>UMBRIAN FRIARS ROAST<br>BLENDED AND WOOD ROASTED IN THE MOUNTAINS NEAR<br>FLORENCE BY THE CLOISTER OF STILLWATER FRIARS</h2>
        <div class="story">
          <p>In their monastery nestled deep in the Mugello mountains the oriental monks blend and roast their coffee. The quiet meadows echo no sound but the occasional movements of a deer or a wild boar in the black pine forests. The delightful song of a meadow lark welcomes the rising sun that lights up the mountain lake where a lonely ancient monastery sits. The mountain peaks begin to twinkle orange in the bright morning sun. A gentle breeze plays with a peaceful cloud of what appears to be a typical mountain fog across the field before the monastery. But it is not a fog. It is the delicious smoke of this morning's dark coffee roast.</p>
          <p>Every morning after prayers, a few of the monks walk down to their roasting barn whose yellow walls glimmer in the sunrise. They are ready to roast the coffee for today's blessed recipients. Curious about how our monks achieve their coffee mastery at 650 meters altitude in the picturesque Mugello mountains near Florence? Rest assured, our master roaster, with over 40 years of expertise, evokes the rich coffee traditions cherished by connoisseurs for fifteen years and beyond.</p>
        </div>
      </div>

      <div class="legal">
        <div class="legal__origin">Italian blend of roasted coffee beans<br>Produced and packaged by the Cloister of Stillwater<br>Priorato di Valleombrosa - Tuscany<br>REA 04518872261</div>
        <div class="legal__care">Keep in a cool<br>and dry place<br>
          <svg width="50" height="20" viewBox="0 0 50 20" aria-label="Dispose responsibly and recycle">
            <rect x="1" y="1" width="18" height="18" fill="none" stroke="#2d2119"/>
            <path d="M6 6h8M7 6l1 10h4l1-10" fill="none" stroke="#2d2119"/>
            <circle cx="36" cy="10" r="8" fill="none" stroke="#2d2119" stroke-width="2"/>
            <path d="M36 4l3 2-3 2z" fill="#2d2119"/>
          </svg>
        </div>
      </div>
      <div class="urls">www.umbrianfriars.coffee | www.stillwatercloister.it</div>
      <div class="net">Net Weight: &nbsp;℮250 gr | 8.8 oz</div>
    </div>
    <div class="best">Best before:</div>
  </div>
</section>

</body>
</html>
```